Design an Exhibition Poster for our Web Application

Our company develops and sells VaultLarkly, a web-based service that helps small businesses to test their web applications for security vulnerabilities.

You can see details of the service at the following page:

https://www.vaultlarkly.example/

We need a poster designed, to be used on an exhibition stand at a professional security conference.
Updates

Project Deadline Extended
Reason: The deadline for this project is being extended because we have, so far, received very few design submissions and they are generally not of the aesthetic quality we are looking for.

Target Market(s)

Tech startups and small / medium sized online businesses

Industry/Entity Type

Security

Requirements
Must have
• [1] Incorporate the VaultLarkly logo (see attached file).

[2] Use the text supplied by us (see attached file).

[3] Use a color scheme that matches the scheme used on our website.

[4] Project the visual theme of cyber security (or protection against cyber crime).
Nice to have
• This is part of a 2-poster set. The project for designing the other poster in the set is also being listed on ArtFolio today. Please look for the project entitled "Design an Exhibition Poster for our Software Product".

Preference will be given to designers who submit a pair of designs that harmonize with each other.

```html
<!DOCTYPE html>
<html lang="en">
<head>
<meta charset="utf-8">
<title>VaultLarkly – Security For Web Startups</title>
<link rel="stylesheet" href="https://fonts.googleapis.com/css2?family=Arimo:wght@400;700&family=Jost:wght@400&display=swap">
<style>
  :root {
    --page: #ffffff;
    --panel: #4b4b4d;
    --band: #505052;
    --arc-shadow: #2b2b2c;
    --tab: #3a3a3b;
    --text-light: #ffffff;
    --text-soft: #e6e6e6;
    --brand-grey: #8d8d8f;
    --brand-mark: #8fb03e;
    --art-steel: #465860;
    --art-slate: #6a7f80;
    --art-moss: #8aa56e;
    --art-lime: #b4d27a;
    --art-glow: rgba(228, 240, 236, 0.75);
  }
  * { box-sizing: border-box; margin: 0; padding: 0; }
  html, body {
    width: 939px; height: 1200px; overflow: hidden;
    background: var(--page);
  }
  .poster {
    position: absolute; left: 26px; top: 26px;
    width: 889px; height: 1150px;
    background: var(--panel);
    overflow: hidden;
    font-family: "Arimo", Arial, sans-serif;
    color: var(--text-light);
  }
  .tagline-band {
    position: absolute; left: 0; top: 0; width: 100%; height: 113px;
    background: var(--band);
    display: flex; align-items: center; justify-content: center;
    font-weight: 700; font-size: 23px; letter-spacing: 0.2px;
  }
  .hero-art {
    position: absolute; left: 0; top: 113px; width: 100%; height: 680px;
    background:
      radial-gradient(ellipse 38% 34% at 66% 28%, var(--art-glow), rgba(228,240,236,0) 72%),
      radial-gradient(ellipse 55% 40% at 30% 45%, rgba(60,74,80,0.55), rgba(60,74,80,0) 75%),
      linear-gradient(180deg, var(--art-steel) 0%, var(--art-slate) 30%, var(--art-moss) 62%, var(--art-lime) 100%);
  }
  .hero-curve {
    position: absolute; left: 0; top: 0; width: 889px; height: 1150px;
  }
  .cta-tab {
    position: absolute; left: 279px; top: 584px; width: 331px; height: 70px;
    background: var(--tab);
    border-radius: 22px 22px 0 0;
    display: flex; align-items: center; justify-content: center;
    font-size: 27px; letter-spacing: 0.3px;
  }
  .headline {
    position: absolute; left: 0; top: 762px; width: 100%;
    text-align: center;
    font-family: "Jost", "Futura", sans-serif; font-weight: 400;
    font-size: 54px; letter-spacing: 0.3px;
  }
  .intro {
    position: absolute; left: 63px; top: 859px; width: 445px;
    font-size: 23.5px; line-height: 31px; color: var(--text-light);
  }
  .features {
    position: absolute; left: 547px; top: 864px; width: 290px;
    list-style: none;
    font-size: 16px; line-height: 19px; color: var(--text-soft);
  }
  .features li { margin-bottom: 21px; }
  .features h3 { font-size: 16px; line-height: 19px; font-weight: 700; color: var(--text-light); }
  .brand {
    position: absolute; left: 65px; top: 997px;
    display: flex; align-items: center; gap: 18px;
  }
  .brand-mark {
    width: 62px; height: 62px; background: var(--brand-mark);
  }
  .brand-name {
    font-size: 50px; font-weight: 700; color: var(--brand-grey);
    letter-spacing: -0.3px;
  }
  .brand-url {
    position: absolute; left: 150px; top: 1060px;
    font-size: 20px; color: var(--brand-grey);
  }
</style>
</head>
<body>
  <main class="poster">
    <header class="tagline-band">Accessible | Affordable | Simple</header>

    <div class="hero-art" role="img" aria-label="Cyber-security illustration: a large steel padlock shattering into flying digital blocks, glowing against a grey-green sky"></div>

    <svg class="hero-curve" viewBox="0 0 889 1150" aria-hidden="true">
      <path d="M0,760 Q444,575 889,730 L889,1150 L0,1150 Z" fill="var(--arc-shadow)"/>
      <path d="M0,790 Q444,625 889,760 L889,1150 L0,1150 Z" fill="var(--panel)"/>
    </svg>

    <div class="cta-tab">Try it Free Today!</div>

    <h1 class="headline">Security For Web Startups</h1>

    <p class="intro">Online website vulnerability scanning that tells you exactly what needs fixing and how to to fix it.</p>

    <ul class="features">
      <li><h3>Accessible</h3>VaultLarkly runs in the cloud and is accessible from any computer, anywhere, any time.</li>
      <li><h3>Affordable</h3>VaultLarkly uses a flexible pay-as-you-go model that will fit any budget.</li>
      <li><h3>Simple</h3>Launch your scan using a simple 3-step wizard and we'll do the rest.</li>
    </ul>

    <div class="brand">
      <span class="brand-mark"></span>
      <span class="brand-name">VaultLarkly</span>
    </div>
    <p class="brand-url">www.vaultlarkly.example</p>
  </main>
</body>
</html>
```